New startup requiring business card

New company needed a business card / logo. Company name is
Zuvrel
Company is providing IT software sales, partnering and consulting services across the APAC region. Catch line is "growing together".
We currently have a feeling yellow as the primary colour given its meaning across the region but open to ideas. Main brief is we want something smart, clean and professional while still leveraging the strength of the name.
A major part of the business is mutually beneficial partnerships, not sure if this helps but maybe visual around linkages between objects.
Also wanting a standard size card, preference is something that will have a D/S cello sheen finish in a matt. But again open to ideas, wow us!
Software

```html
<!DOCTYPE html>
<html lang="en">
<head>
<meta charset="utf-8">
<title>Zuvrel — Business Card</title>
<link rel="stylesheet" href="https://fonts.googleapis.com/css2?family=Questrial&display=swap">
<style>
  :root {
    --backdrop: #2a2a2a;
    --card-black: #0b0b0b;
    --card-yellow: #f2e62a;
    --yellow-text: #e6dc1f;
    --ink: #111111;
    --ink-soft: #2b2b16;
  }
  * { box-sizing: border-box; margin: 0; padding: 0; }
  html, body {
    width: 1200px; height: 900px; overflow: hidden;
    background: var(--backdrop);
    font-family: "Questrial", "Century Gothic", sans-serif;
  }
  .stage { position: relative; width: 1200px; height: 900px; }
  .card {
    position: absolute;
    width: 620px; height: 354px;
    border-radius: 22px;
    box-shadow: 0 18px 40px rgba(0,0,0,0.55);
  }
  .card-front {
    left: 110px; top: 100px; background: var(--card-black);
    display: flex; align-items: center; justify-content: center;
  }
  .card-back {
    left: 480px; top: 470px;
    background: linear-gradient(135deg, #f7ee34 0%, var(--card-yellow) 55%, #d9cf1e 100%);
    color: var(--ink);
  }
  .brand { display: flex; align-items: center; gap: 12px; }
  .brand-dot { width: 38px; height: 38px; border-radius: 50%; flex: none; }
  .brand-name { font-size: 52px; line-height: 1; letter-spacing: 1px; }
  .card-front .brand { color: var(--yellow-text); }
  .card-front .brand-dot { background: var(--yellow-text); }
  .card-back .brand { position: absolute; left: 60px; top: 72px; color: var(--ink); }
  .card-back .brand-dot { background: var(--ink); }
  .holder {
    position: absolute; left: 400px; top: 72px;
    border-left: 4px solid var(--ink); padding-left: 10px;
  }
  .holder-name { font-size: 22px; line-height: 1.1; }
  .holder-role { font-size: 9px; color: var(--ink-soft); margin-top: 3px; }
  .contact {
    position: absolute; display: flex; align-items: center; gap: 8px;
    font-size: 13px; color: var(--ink-soft); white-space: nowrap;
  }
  .contact svg { width: 14px; height: 14px; stroke: var(--ink-soft); fill: none; stroke-width: 1.3; }
  .contact-phone { left: 60px; bottom: 48px; }
  .contact-email { left: 270px; bottom: 48px; }
  .contact-web { right: 50px; bottom: 48px; }
</style>
</head>
<body>
<main class="stage">
  <section class="card card-front">
    <div class="brand">
      <span class="brand-dot"></span>
      <span class="brand-name">zuvrel</span>
    </div>
  </section>

  <section class="card card-back">
    <div class="brand">
      <span class="brand-dot"></span>
      <span class="brand-name">zuvrel</span>
    </div>

    <div class="holder">
      <p class="holder-name">Mara Lindqvist</p>
      <p class="holder-role">general manager</p>
    </div>

    <p class="contact contact-phone">
      <svg viewBox="0 0 14 14"><rect x="3.5" y="1" width="7" height="12" rx="1"/><line x1="6" y1="11" x2="8" y2="11"/></svg>
      012 4815 6230 77
    </p>
    <p class="contact contact-email">
      <svg viewBox="0 0 14 14"><rect x="1" y="3" width="12" height="8"/><polyline points="1,3 7,8 13,3"/></svg>
      mara@zuvrel.com
    </p>
    <p class="contact contact-web">
      <svg viewBox="0 0 14 14"><polyline points="1,7 7,2 13,7"/><polyline points="3,6 3,12 11,12 11,6"/></svg>
      www.zuvrel.com
    </p>
  </section>
</main>
</body>
</html>
```